Geschäftspapier RVB
Zielgruppe
In den letzten Jahren konnten wir uns durch viel Engagement und Ehrgeiz zum Marktführer im Bereich Kaschierungen und Beschichtungen für den Automobilinnenraum in Europa entwickeln. Angeboten werden Rollenware sowie der Zuschnitt und die Weiterverarbeitung von kaschierten Verbundmaterialien und deren Entwicklung für den jeweiligen Einsatzzweck.
Die vielseitig hergestellten Verbundmaterialien aus Textil bis hin zu Kunst- und Echtledern findet man heute in vielen Bauteilen namhafter Automarken, der Flugzeug- und Schienenfahrzeugindustrie sowie in weiteren industriellen, technischen Anwendungen.
Beispiele dafür sind Innenverkleidungen und Sitze im Fahrzeug, Sonnenschutzkomponenten für den privaten und industriellen Bedarf, wie auch Bezüge von Kindersitzen oder medizinische Hygieneprodukte.
Aufgabenstellung
Zur Darstellung des Unternehmens wird ein neues Geschäftspapier gesucht. Dies sollte die folgenden Informationen zum Unternehmen, sowie die Bankkontakte enthalten. Ebenso sollte das vorhandene Firmenlogo integriert werden.
Das Unternehmen produziert hochwertige Textil-Produkte aus den Bereichen Automarken, der Flugzeug- und Schienenfahrzeugindustrie sowie in weiteren industriellen, technischen Anwendungen.
Das Geschäftspapier sollte diese Eigenschaft widerspiegeln und luxuriös, sowie modern erscheinen.
[Optional]
145 Jahre Erfahrung in der Textilveredlung - Führende Kaschier- und Beschichtungstechnologie
145 years of experience in textile processing - Leading technology in lamination and coating
Unternehmensfarbe Grün:
HKS 61 K
70% Cyan
0% Magenta
100% Gelb
75 % Schwarz
optionale Werbefarbe Anthrazit:
77% Cyan
72% Magenta
67% Gelb
84% Schwarz
Schriftart:
Arial

```html
<!DOCTYPE html>
<html lang="de">
<head>
<meta charset="utf-8">
<title>Geschäftspapier RVB</title>
<link href="https://fonts.googleapis.com/css2?family=Arimo:wght@400;700&display=swap" rel="stylesheet">
<style>
  :root {
    --brand-green: #1b4d16;
    --ink: #1c1c1c;
    --ink-soft: #3a3a3a;
    --paper: #ffffff;
    --backdrop: #ececec;
  }
  * { margin: 0; padding: 0; box-sizing: border-box; }
  html, body {
    width: 1200px; height: 898px; overflow: hidden;
    background: var(--backdrop);
    font-family: "Arimo", Arial, sans-serif;
  }
  .letterhead {
    position: absolute; left: 303px; top: 29px;
    width: 594px; height: 840px;
    background: var(--paper);
    box-shadow: 0 4px 18px rgba(0,0,0,.12);
    color: var(--ink);
  }
  .side-bar {
    position: absolute; left: 8px; top: 150px; bottom: 0;
    width: 5px; background: var(--brand-green);
  }
  .brand {
    position: absolute; right: 46px; top: 38px; text-align: right;
    color: var(--brand-green);
  }
  .brand-name { font-size: 34px; font-weight: 400; letter-spacing: 2px; line-height: 1; }
  .brand-claim { font-size: 5.5px; letter-spacing: 2.4px; margin-top: 6px; }
  .sender-line {
    position: absolute; left: 60px; top: 232px;
    font-size: 6.5px; color: var(--brand-green);
  }
  .recipient {
    position: absolute; left: 60px; top: 262px;
    font-size: 9.5px; line-height: 1.35;
  }
  .recipient strong { font-weight: 700; }
  .company-info {
    position: absolute; left: 448px; top: 150px;
    font-size: 6px; line-height: 1.35; color: var(--ink-soft);
  }
  .company-info dt { font-weight: 700; color: var(--ink); }
  .company-info dd { margin-bottom: 7px; }
  .company-info b { color: var(--ink); }
  .product-mark {
    position: absolute; left: 448px; top: 348px; width: 110px; text-align: center;
  }
  .product-mark .dot {
    display: block; width: 6px; height: 6px; border-radius: 50%;
    background: #888; margin: 0 auto 4px;
  }
  .product-name { font-size: 14px; letter-spacing: 3px; color: var(--ink-soft); }
  .product-line { font-size: 5px; color: var(--ink-soft); margin-top: 3px; }
  .footer-rule {
    position: absolute; left: 215px; right: 0; top: 748px;
    height: 1px; background: var(--brand-green);
  }
  .footer {
    position: absolute; left: 215px; right: 20px; top: 756px;
    display: flex; gap: 22px;
    font-size: 5.8px; line-height: 1.35; color: var(--ink-soft);
  }
  .footer-col p { margin-bottom: 6px; }
  .footer-col b { color: var(--ink); }
</style>
</head>
<body>
  <main class="letterhead">
    <div class="side-bar"></div>

    <header class="brand">
      <div class="brand-name">RVB</div>
      <div class="brand-claim">LAMINATION | COATING | COMPONENTS</div>
    </header>

    <p class="sender-line">RVB GmbH • Werkstraße 7 • D-09123 Talbrunn</p>

    <address class="recipient" style="font-style:normal">
      <strong>Mustermann GmbH</strong><br>
      Max Mustermann<br>
      Mustermannstr. 123<br>
      12345 Musterstadt<br>
      Germany
    </address>

    <dl class="company-info">
      <dt>Adresse:</dt>
      <dd>RVB GmbH<br>Werkstraße 7<br>D-09123 Talbrunn</dd>
      <dt>Postanschrift:</dt>
      <dd>Postfach 4410<br>D-09130 Talbrunn</dd>
      <dd><b>Phone:</b> +49 3700 5500 0<br><b>Fax:</b> +49 3700 5500 101</dd>
      <dd><b>Internet:</b> www.rvb-textil.example<br><b>E-Mail:</b> post@rvb-textil.example</dd>
      <dt>Geschäftsführer:</dt>
      <dd>Jonas Keller</dd>
      <dt>Prokura:</dt>
      <dd>Lena Keller<br>Moritz Hain</dd>
    </dl>

    <div class="product-mark">
      <span class="dot"></span>
      <div class="product-name">LUMORA</div>
      <div class="product-line">the new ecological luxury microfiber</div>
    </div>

    <div class="footer-rule"></div>

    <footer class="footer">
      <div class="footer-col">
        <p>Sparkasse Talland<br>IBAN: DE12 3004 1000 2211 0045 18<br>BIC: SPTADED1XXX</p>
        <p>Handelsbank Auental<br>IBAN: DE44 3004 2000 0711 4402 63<br>BIC: HBAUDEFFXXX</p>
      </div>
      <div class="footer-col">
        <p>Vereinsbank Nordtal<br>IBAN: DE71 3004 3000 5120 8830 09<br>BIC: VBNODEMM112</p>
        <p>Genossenschaftsbank Nordtal<br>IBAN: DE38 3004 4000 6604 2119 55<br>BIC: GENODEF1NTL</p>
      </div>
      <div class="footer-col">
        <p>Landesbank West<br>IBAN: DE90 3004 5000 0000 4418 2700<br>BIC: LBWEDE8XXXX</p>
        <p><b>Handelsregister:</b><br>HRB 5521 AG Nordtal<br>UStIDNr.: DE 300418276</p>
      </div>
    </footer>
  </main>
</body>
</html>
```